Zelno Vigor Iron Tempo Multi Vitamin Label Design

We need a label design for our Sports Performance Daily Multi Vitamin specially created and branded for our Zelno Vigor line for the University of Calvoria. The feel is edgy, sports nutrition. Two logos need to be incorporated... Zelno and the Collective Logo attached. The colors should be the official colors of the University of Calvoria. The font may also be the Georgia font... or the Zelno font. Or any font. A hydration product will also be created later on...so this label design may be used on many products. Please utilize the collective logo similar to the use in the attached photo. No official trademark items from the University of Calvoria should be used. Attached is also an image if the bottle (white) that will be used for the vitamin. Please use red, black, grey, white. We are looking for the front design only right now and once selected, will work on the nutrition/back label portion with the artist.

```html
<!DOCTYPE html>
<html lang="en">
<head>
<meta charset="utf-8">
<title>Zelno Sports Performance Daily Multi Vitamin – Front Label</title>
<link href="https://fonts.googleapis.com/css2?family=Montserrat:wght@700;900&family=Permanent+Marker&display=swap" rel="stylesheet">
<style>
  :root {
    --red: #a8182c;
    --red-light: #b8283c;
    --black: #111111;
    --grey: #3a3a3a;
    --white: #ffffff;
    --page: #f2f2f2;
  }
  * { margin: 0; padding: 0; box-sizing: border-box; }
  html, body {
    width: 1200px; height: 675px; overflow: hidden;
    background: var(--page);
    font-family: "Montserrat", Arial, sans-serif;
  }
  .stage {
    width: 1200px; height: 675px;
    display: flex; align-items: center; justify-content: center;
  }
  .label {
    position: relative;
    width: 420px; height: 600px;
    background: linear-gradient(180deg, var(--red-light) 0%, var(--red) 100%);
    overflow: hidden;
    box-shadow: 0 6px 24px rgba(0,0,0,.12);
  }
  .collective-mark {
    position: absolute; top: 26px; left: 0; right: 0;
    display: flex; flex-direction: column; align-items: center; gap: 6px;
  }
  .collective-mark .dot {
    width: 44px; height: 44px; border-radius: 50%;
    background: var(--black);
  }
  .collective-mark .name {
    font-weight: 900; font-size: 11px; letter-spacing: 1.5px;
    color: var(--black); text-transform: uppercase;
  }
  .brand {
    position: absolute; top: 104px; left: 0; right: 0;
    text-align: center;
    font-weight: 900; font-size: 62px; letter-spacing: 2px;
    color: var(--white); text-transform: uppercase;
  }
  .tagline {
    position: absolute; top: 186px; left: 0; right: 0;
    text-align: center;
    font-weight: 900; font-size: 17px; letter-spacing: .5px;
    color: var(--black);
  }
  .tagline .accent { color: var(--white); }
  .headline {
    position: absolute; top: 214px; left: 28px; right: 28px;
    font-family: "Permanent Marker", Impact, "Arial Black", sans-serif;
    font-weight: 400;
    color: var(--white); line-height: .95;
    text-transform: uppercase;
    white-space: nowrap;
  }
  .headline .line1 { display: block; font-size: 76px; padding-left: 26px; }
  .headline .line2 { display: block; font-size: 80px; }
  .count-tag {
    position: absolute; top: 380px; right: 16px;
    background: var(--black); color: var(--white);
    font-weight: 900; font-size: 12px; padding: 5px 10px;
    transform: rotate(-3deg);
  }
  .stats {
    position: absolute; top: 428px; left: 20px; right: 20px;
    display: flex; justify-content: space-around; align-items: center;
  }
  .stat { text-align: center; color: var(--white); }
  .stat .value { display: block; font-weight: 900; font-size: 22px; }
  .stat .unit { display: block; font-weight: 900; font-size: 11px; color: var(--black); margin-top: -2px; }
  .divider { width: 3px; height: 46px; background: var(--white); }
  .footer {
    position: absolute; left: 0; right: 0; bottom: 0; height: 100px;
    background: var(--black);
    display: flex; align-items: center; justify-content: space-between;
    padding: 0 24px;
  }
  .footer::before {
    content: ""; position: absolute; left: 0; right: 0; top: -14px; height: 14px;
    background: var(--white);
  }
  .tablets { text-align: center; }
  .tablets .num { display: block; color: var(--white); font-weight: 900; font-size: 32px; line-height: 1; }
  .tablets .word { display: block; color: var(--red-light); font-weight: 900; font-size: 11px; }
  .collective-name {
    color: var(--red-light); font-weight: 900; font-size: 15px;
    text-align: center; line-height: 1.1; text-transform: uppercase;
  }
  .supplement { text-align: center; font-weight: 900; font-size: 11px; line-height: 1.2; }
  .supplement .top { display: block; color: var(--white); }
  .supplement .bottom { display: block; color: var(--red-light); }
</style>
</head>
<body>
  <main class="stage">
    <section class="label">
      <div class="collective-mark">
        <span class="dot"></span>
        <span class="name">Harbor Town Collective</span>
      </div>

      <h1 class="brand">Zelno</h1>

      <p class="tagline">SPORTS PERFORMANCE <span class="accent">DAILY</span></p>

      <h2 class="headline">
        <span class="line1">Multi</span>
        <span class="line2">Vitamin</span>
      </h2>

      <p class="count-tag">22 VITAMINS &amp; MINIRALS</p>

      <div class="stats">
        <div class="stat"><span class="value">15MG</span><span class="unit">ZINC</span></div>
        <span class="divider"></span>
        <div class="stat"><span class="value">400MG</span><span class="unit">FOLIC ACID</span></div>
        <span class="divider"></span>
        <div class="stat"><span class="value">100%</span><span class="unit">CALCIUM</span></div>
      </div>

      <footer class="footer">
        <div class="tablets"><span class="num">90</span><span class="word">TABLETS</span></div>
        <div class="collective-name">Harbor Town<br>Collective</div>
        <div class="supplement"><span class="top">DIETARY</span><span class="bottom">SUPPLEMENT</span></div>
      </footer>
    </section>
  </main>
</body>
</html>
```